Business Card Design Project

I need a new business card design for my building/development company: Kestrel Ridge Builders.

We specialise in small sub-divisions, multi-story developments and new house builds.
We handle the whole process from concept stage right throught to a fully developed property.
Updates

Target Market(s)

people looking to develop their property and need help. New property buyers

Industry/Entity Type

House

Requirements
Must have
• My logo on both sides:
Side 1: Logo taking up whole side as per old card but with a color/style change.

Side 2: Contact page: include logo but the rest just surprise me!

All contact details will be: (and need to be changable for each employee) I'll inform you of specifics before printing.

Name Surname
Position ie. Managing director
M: insert mobile
E: insert email
P.O. Box 518, Ashwell, Vic, 3094
www.kestrelridgebuilders.com.au

Nice to have
• Colors i'd like: (not necessarily all but this is the basic idea)

Black, blue, grey, silver, white

```html
<!DOCTYPE html>
<html lang="en">
<head>
<meta charset="utf-8">
<title>Kestrel Ridge Builders – Business Card</title>
<link rel="stylesheet" href="https://fonts.googleapis.com/css2?family=Roboto:wght@400;700&display=swap">
<style>
  :root {
    --page: #e9e9e9;
    --card-black: #0b0b0c;
    --sky: #3fb0e6;
    --sky-deep: #1f93cf;
    --silver: #d9dadc;
    --white: #ffffff;
    --ink: #0d1a24;
    --muted: #9aa1a8;
  }
  * { margin: 0; padding: 0; box-sizing: border-box; }
  html, body { width: 1200px; height: 900px; overflow: hidden; }
  body {
    background: var(--page);
    font-family: "Roboto", Arial, sans-serif;
    position: relative;
  }
  .card {
    position: absolute;
    left: 270px;
    width: 660px;
    height: 377px;
    background: var(--card-black);
    overflow: hidden;
    box-shadow: 0 6px 18px rgba(0,0,0,0.25);
  }
  .card--front { top: 52px; }
  .card--back { top: 471px; }

  /* Front side */
  .front-brand {
    position: absolute;
    right: 48px;
    top: 128px;
    text-align: right;
  }
  .brand-name {
    display: flex;
    align-items: center;
    justify-content: flex-end;
    gap: 14px;
    font-weight: 700;
    color: var(--white);
    font-size: 44px;
    line-height: 1;
    letter-spacing: -0.5px;
  }
  .brand-mark {
    width: 30px; height: 30px;
    background: var(--sky);
    flex: none;
  }
  .tagline {
    margin-top: 10px;
    color: var(--white);
    font-size: 15px;
    letter-spacing: 0.3px;
  }
  .front-accent {
    position: absolute;
    left: 0; top: 0;
    width: 100%; height: 100%;
  }

  /* Back side */
  .back-art { position: absolute; inset: 0; }
  .back-brand {
    position: absolute;
    left: 200px;
    top: 60px;
  }
  .back-brand .brand-name { font-size: 34px; justify-content: flex-start; gap: 12px; }
  .back-brand .brand-mark { width: 24px; height: 24px; }
  .back-brand .tagline { font-size: 13px; margin-top: 6px; }

  .holder {
    position: absolute;
    left: 34px;
    top: 290px;
    color: var(--ink);
  }
  .holder-name { font-weight: 700; font-size: 18px; }
  .holder-role { font-size: 13px; margin-top: 3px; }
  .holder-address { font-size: 13px; margin-top: 12px; }

  .contact-divider {
    position: absolute;
    left: 408px;
    top: 218px;
    width: 1px;
    height: 86px;
    background: var(--ink);
    opacity: 0.45;
  }
  .contact-list {
    position: absolute;
    left: 424px;
    top: 222px;
    list-style: none;
    color: var(--ink);
    font-size: 13px;
    line-height: 26px;
  }
  .contact-list .label { color: var(--white); margin-right: 6px; }
</style>
</head>
<body>

<section class="card card--front" aria-label="Card front">
  <svg class="front-accent" viewBox="0 0 660 377" aria-hidden="true">
    <path d="M0,300 C200,300 420,330 660,280 L660,300 C420,350 200,322 0,322 Z" fill="var(--silver)"/>
    <path d="M0,322 C200,322 420,350 660,300 L660,377 L0,377 Z" fill="var(--sky)"/>
  </svg>
  <div class="front-brand">
    <div class="brand-name"><span class="brand-mark"></span>Kestrel Ridge Builders</div>
    <p class="tagline">renovation-construction-development</p>
  </div>
</section>

<section class="card card--back" aria-label="Card back">
  <svg class="back-art" viewBox="0 0 660 377" aria-hidden="true">
    <defs>
      <linearGradient id="band" x1="0" y1="0" x2="0" y2="1">
        <stop offset="0" stop-color="var(--sky)"/>
        <stop offset="1" stop-color="var(--sky-deep)"/>
      </linearGradient>
    </defs>
    <path d="M0,238 C240,242 470,206 660,126 L660,154 C470,234 240,262 0,260 Z" fill="var(--silver)"/>
    <path d="M0,260 C240,262 470,234 660,154 L660,377 L0,377 Z" fill="url(#band)"/>
  </svg>

  <div class="back-brand">
    <div class="brand-name"><span class="brand-mark"></span>Kestrel Ridge Builders</div>
    <p class="tagline">renovation-construction-development</p>
  </div>

  <div class="holder">
    <p class="holder-name">Maren Holloway</p>
    <p class="holder-role">Managing director</p>
    <p class="holder-address">P.O. Box 518, Ashwell, Vic, 3094</p>
  </div>

  <span class="contact-divider"></span>
  <ul class="contact-list">
    <li><span class="label">M:</span>0000 000 0000</li>
    <li><span class="label">E:</span>info@kestrelridgebuilders.com.au</li>
    <li><span class="label">W:</span>www.kestrelridgebuilders.com.au</li>
  </ul>
</section>

</body>
</html>
```